Cat-products company needs smart, yet endearing, business card

We need a business card design for a new, but up-and-running, business based in Honolulu, Hawaii. The business is Purrlane Nest Co. Our first product is the most environmentally-friendly cat grass kit ever seen on the planet. Future products, currently in the R&D phase, will include a variety of exciting cat scratchers. We also do consulting work to help apartment-dwellers make their home more cat-friendly and, in the future, plan on doing full, custom installs of structure to create high walkways for cats.

Target Market(s)

Middle-aged, apartment-dwelling, middle-class workers who own 1 or more cats and who dote on them.

Industry/Entity Type

Pet Care

Contact Information for Business Card

A striking, professional, yet warm and friendly design is what we're after.

Font styles to use
Serif
Sans Serif
Other font styles liked:
• Comfortaa

Colors

Designer to choose colors to be used in the design.

Requirements
Must have
• The company logo: (see attachment)
• The company name: Purrlane Nest Co
• The web address: www.purrlanenestco.example
• Email: support@purrlanenestco.example
• Phone: +1 (808) 555 0172
• Update (Fri Jun 30 3017 7:45pm Hawaii Time) I would like, is possible, uploaded picture of the cat grass kit on the back of the card with some text along the lines of: Purrlane Nest Co - Where The Freshest Kitty Sprouts Begin
Nice to have
• A cat picture, cartoon, real or silhouette that illustrates cats in action and/or relaxing; ie using the apartment space to live, play and relax in and being well-contented.
• Most of the website is done in the font: Comfortaa. It might be nice to continue using this for brand consistency.
Should not have
• Hard-to-read fonts.

```html
<!DOCTYPE html>
<html lang="en">
<head>
<meta charset="utf-8">
<title>Purrlane Nest Co — Business Card</title>
<link rel="stylesheet" href="https://fonts.googleapis.com/css2?family=Montserrat:wght@300;400;700&family=Libre+Baskerville:wght@700&display=swap">
<style>
  :root {
    --backdrop: #d4e7f6;
    --card: #ffffff;
    --ink: #2f2a28;
    --brown: #55302b;
    --amber: #f6b21f;
    --paw: #fee4b6;
    --photo-dark: #9b9697;
    --photo-light: #efe6dd;
    --photo-fur: #e9c79d;
  }
  * { margin: 0; padding: 0; box-sizing: border-box; }
  html, body {
    width: 1200px; height: 935px; overflow: hidden;
    background: var(--backdrop);
  }
  .canvas { position: relative; width: 1200px; height: 935px; }
  .card {
    position: absolute; left: 252px; width: 658px; height: 376px;
    border-radius: 16px; overflow: hidden;
    box-shadow: 8px 9px 10px rgba(40, 50, 60, 0.45);
  }
  .card--front { top: 54px; background: var(--card); }
  .card--back { top: 498px; }

  .paw-decoration {
    position: absolute; left: 350px; top: 70px; width: 320px; height: 320px;
    background: radial-gradient(ellipse at 70% 70%, var(--paw) 0%, var(--paw) 45%, rgba(254,228,182,0.55) 62%, rgba(254,228,182,0) 75%);
  }

  .brand-mark {
    position: absolute; left: 40px; top: 168px; width: 180px;
    display: flex; align-items: center; gap: 8px;
  }
  .brand-mark__dot {
    width: 14px; height: 14px; border-radius: 50%; background: var(--amber); flex: none;
  }
  .brand-mark__name {
    font-family: "Montserrat", sans-serif; font-weight: 700;
    font-size: 19px; color: var(--amber); white-space: nowrap;
  }

  .divider {
    position: absolute; left: 268px; top: 117px; width: 1.5px; height: 156px;
    background: var(--ink);
  }

  .company-name {
    position: absolute; left: 326px; top: 129px;
    font-family: "Libre Baskerville", serif; font-weight: 700;
    font-size: 22px; color: var(--ink); white-space: nowrap;
  }

  .contact-list { position: absolute; left: 330px; top: 186px; list-style: none; }
  .contact-list__item {
    display: flex; align-items: center; height: 22px;
    font-family: "Montserrat", sans-serif; font-weight: 400;
    font-size: 17px; color: var(--ink); white-space: nowrap;
  }
  .contact-list__icon { width: 12px; height: 12px; margin-right: 12px; flex: none; }
  .highlight { color: var(--amber); }

  .back-photo {
    position: absolute; inset: 0;
    background:
      radial-gradient(ellipse at 30% 60%, var(--photo-light) 0%, rgba(239,230,221,0) 45%),
      radial-gradient(ellipse at 65% 45%, var(--photo-fur) 0%, rgba(233,199,157,0) 40%),
      linear-gradient(180deg, var(--photo-dark) 0%, #b9b3b0 50%, #cfcac6 100%);
  }
  .back-name {
    position: absolute; left: 0; right: 0; top: 308px; text-align: center;
    font-family: "Montserrat", sans-serif; font-weight: 700;
    font-size: 34px; color: var(--amber);
  }
</style>
</head>
<body>
<div class="canvas">
  <section class="card card--front">
    <div class="paw-decoration" role="img" aria-label="Large faint paw print decoration"></div>

    <div class="brand-mark">
      <span class="brand-mark__dot"></span>
      <span class="brand-mark__name">Purrlane Nest Co</span>
    </div>

    <div class="divider"></div>

    <h1 class="company-name">Purrlane Nest Co</h1>

    <ul class="contact-list">
      <li class="contact-list__item">
        <svg class="contact-list__icon" viewBox="0 0 12 12" fill="none" stroke="#f6b21f" stroke-width="1.3" stroke-linecap="round"><path d="M3 1.5 L4.5 3.5 L3.6 4.6 Q4.8 7.5 7.4 8.4 L8.5 7.5 L10.5 9 L9.5 10.5 Q4 10 1.5 3 Z"/></svg>
        www.purrlanenestco.example
      </li>
      <li class="contact-list__item">
        <svg class="contact-list__icon" viewBox="0 0 12 12" fill="none" stroke="#f6b21f" stroke-width="1.2"><rect x="1" y="2.5" width="10" height="7" rx="0.8"/><path d="M1.3 3 L6 6.6 L10.7 3"/></svg>
        <span>support@<span class="highlight">purrlanenestco</span>.example</span>
      </li>
      <li class="contact-list__item">
        <svg class="contact-list__icon" viewBox="0 0 12 12" fill="none" stroke="#f6b21f" stroke-width="1"><circle cx="6" cy="6" r="5"/><ellipse cx="6" cy="6" rx="2.2" ry="5"/><path d="M1 6 H11 M2 3.3 H10 M2 8.7 H10"/></svg>
        +1 (808) 555 0172
      </li>
    </ul>
  </section>

  <section class="card card--back">
    <div class="back-photo" role="img" aria-label="Soft-toned photo of two fluffy kittens resting on a grey blanket"></div>
    <p class="back-name">Purrlane Nest Co</p>
  </section>
</div>
</body>
</html>
```